Heart Rate Game Display Graphic

We need a unique layout / info-graphic for our heart rate software to display an individuals hear rate, HR%, and other data together within a larger class of up to 40 other users. Graphics should be colorful, dynamic, and intuitive.

Target Market(s)

Group Fitness Classes

Font styles to use
Sans Serif

Colors

Designer to choose colors to be used in the design.

Requirements
Must have
• Individual Box must contain data field or graphic representation of:
• User Name
• Heart Rate %
• Points Earned / % Accuracy
Nice to have
• thinking other shape design that easily integrates with 40+ of the same shape. Looking for depth of design and or some 3d visualizations. Competing companies:
• https://www.pulsevane.org/
• https://www.trovo.com/
• https://www.kestra.com/us-en/club
• https://bravulo.com/
• https://dornaly.fit/personal-trainer/
• https://www.quelvanta.io/Solutions/Heart-Rate-Training
• http://wamble.corvinladesystems.com/
• https://pell-tander.com/explore/pell-tander-indoor-cycling-app/
Should not have
• should NOT be just be plain squares representing each client.

```html
<!DOCTYPE html>
<html lang="en">
<head>
<meta charset="utf-8">
<title>Heart Rate Class Board</title>
<link rel="stylesheet" href="https://fonts.googleapis.com/css2?family=Oswald:wght@400;500&display=swap">
<style>
  :root {
    --bg: #232e45;
    --ink: #ffffff;
    --pink: #f0306a;
    --orange: #f5a623;
    --green: #8cb92c;
    --purple: #8b4aa0;
    --blue: #3a77b0;
    --heart: #c21f4b;
  }
  * { margin: 0; padding: 0; box-sizing: border-box; }
  html, body { width: 1200px; height: 661px; overflow: hidden; background: var(--bg); }
  .board { position: relative; width: 1200px; height: 661px; font-family: "Oswald", sans-serif; color: var(--ink); }

  .zone-rail { position: absolute; left: 33px; top: 0; width: 16px; height: 661px; }
  .zone-line { position: absolute; left: 6px; top: 82px; width: 5px; height: 510px;
    background: linear-gradient(to bottom, var(--pink) 0%, var(--orange) 25%, var(--green) 50%, var(--purple) 75%, var(--blue) 100%); }
  .zone-dot { position: absolute; left: -7px; width: 30px; height: 30px; border-radius: 50%; }
  .zone-dot.z1 { top: 67px; background: var(--pink); }
  .zone-dot.z2 { top: 194px; background: var(--orange); }
  .zone-dot.z3 { top: 319px; background: var(--green); }
  .zone-dot.z4 { top: 447px; background: var(--purple); }
  .zone-dot.z5 { top: 577px; background: var(--blue); }

  .roster { position: absolute; left: 63px; top: 33px; display: grid;
    grid-template-columns: repeat(10, 113px); grid-auto-rows: 152.6px; }
  .athlete { display: flex; flex-direction: column; align-items: center; }
  .athlete-name { height: 24px; line-height: 24px; font-size: 17px; font-weight: 500; letter-spacing: 0.5px; margin-bottom: 14px; }
  .dial { width: 100px; height: 100px; overflow: visible; }
  .dial-level { fill: var(--tone); }
  .dial-ring { fill: none; stroke: var(--ink); stroke-width: 2.2; }
  .dial-badge { fill: var(--tone); }
  .dial-pct { font-family: "Oswald", sans-serif; font-size: 12px; fill: var(--ink); text-anchor: middle; }
  .heart-shape { fill: var(--heart); stroke: var(--ink); stroke-width: 1.6; }
  .dial-bpm { font-family: "Oswald", sans-serif; font-size: 11.5px; fill: var(--ink); text-anchor: middle; }

  .tone-pink { --tone: var(--pink); }
  .tone-orange { --tone: var(--orange); }
  .tone-green { --tone: var(--green); }
  .tone-purple { --tone: var(--purple); }
  .tone-blue { --tone: var(--blue); }
</style>
</head>
<body>
<svg width="0" height="0" style="position:absolute" aria-hidden="true">
  <defs>
    <clipPath id="dial-clip"><circle cx="50" cy="50" r="42"/></clipPath>
    <path id="heart" class="heart-shape" d="M21 99 C8 90 4 83 4 78 C4 72 9 69 13 69 C17 69 20 71 21 74 C22 71 25 69 29 69 C33 69 38 72 38 78 C38 83 34 90 21 99Z"/>
  </defs>
</svg>

<main class="board">
  <div class="zone-rail" aria-label="Heart rate zones">
    <div class="zone-line"></div>
    <span class="zone-dot z1"></span><span class="zone-dot z2"></span><span class="zone-dot z3"></span><span class="zone-dot z4"></span><span class="zone-dot z5"></span>
  </div>

  <section class="roster">
    <!-- row 1 -->
    <div class="athlete tone-purple"><p class="athlete-name">THOMAS</p><svg class="dial" viewBox="0 0 100 100"><g clip-path="url(#dial-clip)"><rect class="dial-level" x="0" y="70" width="100" height="40" rx="10"/></g><circle class="dial-ring" cx="50" cy="50" r="46"/><circle class="dial-badge" cx="73" cy="23" r="16"/><text class="dial-pct" x="73" y="27">56%</text><use href="#heart"/><text class="dial-bpm" x="21" y="85">160</text></svg></div>
    <div class="athlete tone-blue"><p class="athlete-name">JACKSON</p><svg class="dial" viewBox="0 0 100 100"><g clip-path="url(#dial-clip)"><rect class="dial-level" x="0" y="68" width="100" height="40" rx="10"/></g><circle class="dial-ring" cx="50" cy="50" r="46"/><circle class="dial-badge" cx="73" cy="23" r="16"/><text class="dial-pct" x="73" y="27">42%</text><use href="#heart"/><text class="dial-bpm" x="21" y="85">115</text></svg></div>
    <div class="athlete tone-pink"><p class="athlete-name">WILSON</p><svg class="dial" viewBox="0 0 100 100"><g clip-path="url(#dial-clip)"><rect class="dial-level" x="0" y="28" width="100" height="80" rx="10"/></g><circle class="dial-ring" cx="50" cy="50" r="46"/><circle class="dial-badge" cx="73" cy="23" r="16"/><text class="dial-pct" x="73" y="27">98%</text><use href="#heart"/><text class="dial-bpm" x="21" y="85">186</text></svg></div>
    <div class="athlete tone-green"><p class="athlete-name">SMITH</p><svg class="dial" viewBox="0 0 100 100"><g clip-path="url(#dial-clip)"><rect class="dial-level" x="0" y="55" width="100" height="60" rx="10"/></g><circle class="dial-ring" cx="50" cy="50" r="46"/><circle class="dial-badge" cx="73" cy="23" r="16"/><text class="dial-pct" x="73" y="27">72%</text><use href="#heart"/><text class="dial-bpm" x="21" y="85">149</text></svg></div>
    <div class="athlete tone-green"><p class="athlete-name">SMITH</p><svg class="dial" viewBox="0 0 100 100"><g clip-path="url(#dial-clip)"><rect class="dial-level" x="0" y="55" width="100" height="60" rx="10"/></g><circle class="dial-ring" cx="50" cy="50" r="46"/><circle class="dial-badge" cx="73" cy="23" r="16"/><text class="dial-pct" x="73" y="27">72%</text><use href="#heart"/><text class="dial-bpm" x="21" y="85">149</text></svg></div>
    <div class="athlete tone-orange"><p class="athlete-name">DAVIS</p><svg class="dial" viewBox="0 0 100 100"><g clip-path="url(#dial-clip)"><rect class="dial-level" x="0" y="45" width="100" height="70" rx="10"/></g><circle class="dial-ring" cx="50" cy="50" r="46"/><circle class="dial-badge" cx="73" cy="23" r="16"/><text class="dial-pct" x="73" y="27">82%</text><use href="#heart"/><text class="dial-bpm" x="21" y="85">161</text></svg></div>
    <div class="athlete tone-blue"><p class="athlete-name">JACKSON</p><svg class="dial" viewBox="0 0 100 100"><g clip-path="url(#dial-clip)"><rect class="dial-level" x="0" y="68" width="100" height="40" rx="10"/></g><circle class="dial-ring" cx="50" cy="50" r="46"/><circle class="dial-badge" cx="73" cy="23" r="16"/><text class="dial-pct" x="73" y="27">42%</text><use href="#heart"/><text class="dial-bpm" x="21" y="85">115</text></svg></div>
    <div class="athlete tone-orange"><p class="athlete-name">ANDERSON</p><svg class="dial" viewBox="0 0 100 100"><g clip-path="url(#dial-clip)"><rect class="dial-level" x="0" y="45" width="100" height="70" rx="10"/></g><circle class="dial-ring" cx="50" cy="50" r="46"/><circle class="dial-badge" cx="73" cy="23" r="16"/><text class="dial-pct" x="73" y="27">82%</text><use href="#heart"/><text class="dial-bpm" x="21" y="85">164</text></svg></div>
    <div class="athlete tone-pink"><p class="athlete-name">WILSON</p><svg class="dial" viewBox="0 0 100 100"><g clip-path="url(#dial-clip)"><rect class="dial-level" x="0" y="28" width="100" height="80" rx="10"/></g><circle class="dial-ring" cx="50" cy="50" r="46"/><circle class="dial-badge" cx="73" cy="23" r="16"/><text class="dial-pct" x="73" y="27">98%</text><use href="#heart"/><text class="dial-bpm" x="21" y="85">186</text></svg></div>
    <div class="athlete tone-green"><p class="athlete-name">SMITH</p><svg class="dial" viewBox="0 0 100 100"><g clip-path="url(#dial-clip)"><rect class="dial-level" x="0" y="55" width="100" height="60" rx="10"/></g><circle class="dial-ring" cx="50" cy="50" r="46"/><circle class="dial-badge" cx="73" cy="23" r="16"/><text class="dial-pct" x="73" y="27">72%</text><use href="#heart"/><text class="dial-bpm" x="21" y="85">149</text></svg></div>

    <!-- row 2 -->
    <div class="athlete tone-orange"><p class="athlete-name">BROWN</p><svg class="dial" viewBox="0 0 100 100"><g clip-path="url(#dial-clip)"><rect class="dial-level" x="0" y="45" width="100" height="70" rx="10"/></g><circle class="dial-ring" cx="50" cy="50" r="46"/><circle class="dial-badge" cx="73" cy="23" r="16"/><text class="dial-pct" x="73" y="27">82%</text><use href="#heart"/><text class="dial-bpm" x="21" y="85">160</text></svg></div>
    <div class="athlete tone-green"><p class="athlete-name">MILLER</p><svg class="dial" viewBox="0 0 100 100"><g clip-path="url(#dial-clip)"><rect class="dial-level" x="0" y="52" width="100" height="60" rx="10"/></g><circle class="dial-ring" cx="50" cy="50" r="46"/><circle class="dial-badge" cx="73" cy="23" r="16"/><text class="dial-pct" x="73" y="27">75%</text><use href="#heart"/><text class="dial-bpm" x="21" y="85">145</text></svg></div>
    <div class="athlete tone-green"><p class="athlete-name">SMITH</p><svg class="dial" viewBox="0 0 100 100"><g clip-path="url(#dial-clip)"><rect class="dial-level" x="0" y="55" width="100" height="60" rx="10"/></g><circle class="dial-ring" cx="50" cy="50" r="46"/><circle class="dial-badge" cx="73" cy="23" r="16"/><text class="dial-pct" x="73" y="27">72%</text><use href="#heart"/><text class="dial-bpm" x="21" y="85">149</text></svg></div>
    <div class="athlete tone-orange"><p class="athlete-name">DAVIS</p><svg class="dial" viewBox="0 0 100 100"><g clip-path="url(#dial-clip)"><rect class="dial-level" x="0" y="45" width="100" height="70" rx="10"/></g><circle class="dial-ring" cx="50" cy="50" r="46"/><circle class="dial-badge" cx="73" cy="23" r="16"/><text class="dial-pct" x="73" y="27">82%</text><use href="#heart"/><text class="dial-bpm" x="21" y="85">161</text></svg></div>
    <div class="athlete tone-blue"><p class="athlete-name">JACKSON</p><svg class="dial" viewBox="0 0 100 100"><g clip-path="url(#dial-clip)"><rect class="dial-level" x="0" y="68" width="100" height="40" rx="10"/></g><circle class="dial-ring" cx="50" cy="50" r="46"/><circle class="dial-badge" cx="73" cy="23" r="16"/><text class="dial-pct" x="73" y="27">42%</text><use href="#heart"/><text class="dial-bpm" x="21" y="85">115</text></svg></div>
    <div class="athlete tone-orange"><p class="athlete-name">ANDERSON</p><svg class="dial" viewBox="0 0 100 100"><g clip-path="url(#dial-clip)"><rect class="dial-level" x="0" y="45" width="100" height="70" rx="10"/></g><circle class="dial-ring" cx="50" cy="50" r="46"/><circle class="dial-badge" cx="73" cy="23" r="16"/><text class="dial-pct" x="73" y="27">82%</text><use href="#heart"/><text class="dial-bpm" x="21" y="85">164</text></svg></div>
    <div class="athlete tone-pink"><p class="athlete-name">WILSON</p><svg class="dial" viewBox="0 0 100 100"><g clip-path="url(#dial-clip)"><rect class="dial-level" x="0" y="28" width="100" height="80" rx="10"/></g><circle class="dial-ring" cx="50" cy="50" r="46"/><circle class="dial-badge" cx="73" cy="23" r="16"/><text class="dial-pct" x="73" y="27">98%</text><use href="#heart"/><text class="dial-bpm" x="21" y="85">186</text></svg></div>
    <div class="athlete tone-green"><p class="athlete-name">SMITH</p><svg class="dial" viewBox="0 0 100 100"><g clip-path="url(#dial-clip)"><rect class="dial-level" x="0" y="55" width="100" height="60" rx="10"/></g><circle class="dial-ring" cx="50" cy="50" r="46"/><circle class="dial-badge" cx="73" cy="23" r="16"/><text class="dial-pct" x="73" y="27">72%</text><use href="#heart"/><text class="dial-bpm" x="21" y="85">149</text></svg></div>
    <div class="athlete tone-orange"><p class="athlete-name">DAVIS</p><svg class="dial" viewBox="0 0 100 100"><g clip-path="url(#dial-clip)"><rect class="dial-level" x="0" y="45" width="100" height="70" rx="10"/></g><circle class="dial-ring" cx="50" cy="50" r="46"/><circle class="dial-badge" cx="73" cy="23" r="16"/><text class="dial-pct" x="73" y="27">82%</text><use href="#heart"/><text class="dial-bpm" x="21" y="85">161</text></svg></div>
    <div class="athlete tone-blue"><p class="athlete-name">JACKSON</p><svg class="dial" viewBox="0 0 100 100"><g clip-path="url(#dial-clip)"><rect class="dial-level" x="0" y="68" width="100" height="40" rx="10"/></g><circle class="dial-ring" cx="50" cy="50" r="46"/><circle class="dial-badge" cx="73" cy="23" r="16"/><text class="dial-pct" x="73" y="27">42%</text><use href="#heart"/><text class="dial-bpm" x="21" y="85">115</text></svg></div>

    <!-- row 3 -->
    <div class="athlete tone-pink"><p class="athlete-name">WILSON</p><svg class="dial" viewBox="0 0 100 100"><g clip-path="url(#dial-clip)"><rect class="dial-level" x="0" y="28" width="100" height="80" rx="10"/></g><circle class="dial-ring" cx="50" cy="50" r="46"/><circle class="dial-badge" cx="73" cy="23" r="16"/><text class="dial-pct" x="73" y="27">98%</text><use href="#heart"/><text class="dial-bpm" x="21" y="85">186</text></svg></div>
    <div class="athlete tone-orange"><p class="athlete-name">ANDERSON</p><svg class="dial" viewBox="0 0 100 100"><g clip-path="url(#dial-clip)"><rect class="dial-level" x="0" y="45" width="100" height="70" rx="10"/></g><circle class="dial-ring" cx="50" cy="50" r="46"/><circle class="dial-badge" cx="73" cy="23" r="16"/><text class="dial-pct" x="73" y="27">82%</text><use href="#heart"/><text class="dial-bpm" x="21" y="85">164</text></svg></div>
    <div class="athlete tone-pink"><p class="athlete-name">WILSON</p><svg class="dial" viewBox="0 0 100 100"><g clip-path="url(#dial-clip)"><rect class="dial-level" x="0" y="28" width="100" height="80" rx="10"/></g><circle class="dial-ring" cx="50" cy="50" r="46"/><circle class="dial-badge" cx="73" cy="23" r="16"/><text class="dial-pct" x="73" y="27">98%</text><use href="#heart"/><text class="dial-bpm" x="21" y="85">186</text></svg></div>
    <div class="athlete tone-green"><p class="athlete-name">SMITH</p><svg class="dial" viewBox="0 0 100 100"><g clip-path="url(#dial-clip)"><rect class="dial-level" x="0" y="55" width="100" height="60" rx="10"/></g><circle class="dial-ring" cx="50" cy="50" r="46"/><circle class="dial-badge" cx="73" cy="23" r="16"/><text class="dial-pct" x="73" y="27">72%</text><use href="#heart"/><text class="dial-bpm" x="21" y="85">149</text></svg></div>
    <div class="athlete tone-green"><p class="athlete-name">SMITH</p><svg class="dial" viewBox="0 0 100 100"><g clip-path="url(#dial-clip)"><rect class="dial-level" x="0" y="55" width="100" height="60" rx="10"/></g><circle class="dial-ring" cx="50" cy="50" r="46"/><circle class="dial-badge" cx="73" cy="23" r="16"/><text class="dial-pct" x="73" y="27">72%</text><use href="#heart"/><text class="dial-bpm" x="21" y="85">149</text></svg></div>
    <div class="athlete tone-orange"><p class="athlete-name">DAVIS</p><svg class="dial" viewBox="0 0 100 100"><g clip-path="url(#dial-clip)"><rect class="dial-level" x="0" y="45" width="100" height="70" rx="10"/></g><circle class="dial-ring" cx="50" cy="50" r="46"/><circle class="dial-badge" cx="73" cy="23" r="16"/><text class="dial-pct" x="73" y="27">82%</text><use href="#heart"/><text class="dial-bpm" x="21" y="85">161</text></svg></div>
    <div class="athlete tone-blue"><p class="athlete-name">JACKSON</p><svg class="dial" viewBox="0 0 100 100"><g clip-path="url(#dial-clip)"><rect class="dial-level" x="0" y="68" width="100" height="40" rx="10"/></g><circle class="dial-ring" cx="50" cy="50" r="46"/><circle class="dial-badge" cx="73" cy="23" r="16"/><text class="dial-pct" x="73" y="27">42%</text><use href="#heart"/><text class="dial-bpm" x="21" y="85">115</text></svg></div>
    <div class="athlete tone-orange"><p class="athlete-name">ANDERSON</p><svg class="dial" viewBox="0 0 100 100"><g clip-path="url(#dial-clip)"><rect class="dial-level" x="0" y="45" width="100" height="70" rx="10"/></g><circle class="dial-ring" cx="50" cy="50" r="46"/><circle class="dial-badge" cx="73" cy="23" r="16"/><text class="dial-pct" x="73" y="27">82%</text><use href="#heart"/><text class="dial-bpm" x="21" y="85">164</text></svg></div>
    <div class="athlete tone-pink"><p class="athlete-name">WILSON</p><svg class="dial" viewBox="0 0 100 100"><g clip-path="url(#dial-clip)"><rect class="dial-level" x="0" y="28" width="100" height="80" rx="10"/></g><circle class="dial-ring" cx="50" cy="50" r="46"/><circle class="dial-badge" cx="73" cy="23" r="16"/><text class="dial-pct" x="73" y="27">98%</text><use href="#heart"/><text class="dial-bpm" x="21" y="85">186</text></svg></div>
    <div class="athlete tone-green"><p class="athlete-name">SMITH</p><svg class="dial" viewBox="0 0 100 100"><g clip-path="url(#dial-clip)"><rect class="dial-level" x="0" y="55" width="100" height="60" rx="10"/></g><circle class="dial-ring" cx="50" cy="50" r="46"/><circle class="dial-badge" cx="73" cy="23" r="16"/><text class="dial-pct" x="73" y="27">72%</text><use href="#heart"/><text class="dial-bpm" x="21" y="85">149</text></svg></div>

    <!-- row 4 -->
    <div class="athlete tone-pink"><p class="athlete-name">WILSON</p><svg class="dial" viewBox="0 0 100 100"><g clip-path="url(#dial-clip)"><rect class="dial-level" x="0" y="28" width="100" height="80" rx="10"/></g><circle class="dial-ring" cx="50" cy="50" r="46"/><circle class="dial-badge" cx="73" cy="23" r="16"/><text class="dial-pct" x="73" y="27">98%</text><use href="#heart"/><text class="dial-bpm" x="21" y="85">186</text></svg></div>
    <div class="athlete tone-blue"><p class="athlete-name">JACKSON</p><svg class="dial" viewBox="0 0 100 100"><g clip-path="url(#dial-clip)"><rect class="dial-level" x="0" y="74" width="100" height="40" rx="10"/></g><circle class="dial-ring" cx="50" cy="50" r="46"/><circle class="dial-badge" cx="73" cy="23" r="16"/><text class="dial-pct" x="73" y="27">42%</text><use href="#heart"/><text class="dial-bpm" x="21" y="85">115</text></svg></div>
    <div class="athlete tone-pink"><p class="athlete-name">WILSON</p><svg class="dial" viewBox="0 0 100 100"><g clip-path="url(#dial-clip)"><rect class="dial-level" x="0" y="28" width="100" height="80" rx="10"/></g><circle class="dial-ring" cx="50" cy="50" r="46"/><circle class="dial-badge" cx="73" cy="23" r="16"/><text class="dial-pct" x="73" y="27">98%</text><use href="#heart"/><text class="dial-bpm" x="21" y="85">186</text></svg></div>
    <div class="athlete tone-green"><p class="athlete-name">SMITH</p><svg class="dial" viewBox="0 0 100 100"><g clip-path="url(#dial-clip)"><rect class="dial-level" x="0" y="55" width="100" height="60" rx="10"/></g><circle class="dial-ring" cx="50" cy="50" r="46"/><circle class="dial-badge" cx="73" cy="23" r="16"/><text class="dial-pct" x="73" y="27">72%</text><use href="#heart"/><text class="dial-bpm" x="21" y="85">149</text></svg></div>
    <div class="athlete tone-green"><p class="athlete-name">SMITH</p><svg class="dial" viewBox="0 0 100 100"><g clip-path="url(#dial-clip)"><rect class="dial-level" x="0" y="55" width="100" height="60" rx="10"/></g><circle class="dial-ring" cx="50" cy="50" r="46"/><circle class="dial-badge" cx="73" cy="23" r="16"/><text class="dial-pct" x="73" y="27">72%</text><use href="#heart"/><text class="dial-bpm" x="21" y="85">149</text></svg></div>
    <div class="athlete tone-orange"><p class="athlete-name">DAVIS</p><svg class="dial" viewBox="0 0 100 100"><g clip-path="url(#dial-clip)"><rect class="dial-level" x="0" y="45" width="100" height="70" rx="10"/></g><circle class="dial-ring" cx="50" cy="50" r="46"/><circle class="dial-badge" cx="73" cy="23" r="16"/><text class="dial-pct" x="73" y="27">82%</text><use href="#heart"/><text class="dial-bpm" x="21" y="85">161</text></svg></div>
    <div class="athlete tone-blue"><p class="athlete-name">JACKSON</p><svg class="dial" viewBox="0 0 100 100"><g clip-path="url(#dial-clip)"><rect class="dial-level" x="0" y="68" width="100" height="40" rx="10"/></g><circle class="dial-ring" cx="50" cy="50" r="46"/><circle class="dial-badge" cx="73" cy="23" r="16"/><text class="dial-pct" x="73" y="27">42%</text><use href="#heart"/><text class="dial-bpm" x="21" y="85">115</text></svg></div>
    <div class="athlete tone-orange"><p class="athlete-name">ANDERSON</p><svg class="dial" viewBox="0 0 100 100"><g clip-path="url(#dial-clip)"><rect class="dial-level" x="0" y="45" width="100" height="70" rx="10"/></g><circle class="dial-ring" cx="50" cy="50" r="46"/><circle class="dial-badge" cx="73" cy="23" r="16"/><text class="dial-pct" x="73" y="27">82%</text><use href="#heart"/><text class="dial-bpm" x="21" y="85">164</text></svg></div>
    <div class="athlete tone-pink"><p class="athlete-name">WILSON</p><svg class="dial" viewBox="0 0 100 100"><g clip-path="url(#dial-clip)"><rect class="dial-level" x="0" y="28" width="100" height="80" rx="10"/></g><circle class="dial-ring" cx="50" cy="50" r="46"/><circle class="dial-badge" cx="73" cy="23" r="16"/><text class="dial-pct" x="73" y="27">98%</text><use href="#heart"/><text class="dial-bpm" x="21" y="85">186</text></svg></div>
    <div class="athlete tone-green"><p class="athlete-name">SMITH</p><svg class="dial" viewBox="0 0 100 100"><g clip-path="url(#dial-clip)"><rect class="dial-level" x="0" y="55" width="100" height="60" rx="10"/></g><circle class="dial-ring" cx="50" cy="50" r="46"/><circle class="dial-badge" cx="73" cy="23" r="16"/><text class="dial-pct" x="73" y="27">72%</text><use href="#heart"/><text class="dial-bpm" x="21" y="85">149</text></svg></div>
  </section>
</main>
</body>
</html>
```